Harbor Crest Vitality.com Landing Page

Create a well designed home/landing page using that communicates the feeling of Harbor Crest Vitality with this sections that scroll from top to bottom -
Top section - Displays "Harbor Crest Vitality" with space for embedded YouTube video.

The following sections follow the top section -
Assess your current Harbor Crest Vitality. Complete our free life balance assessment to identify key areas where you you will most benefit.
"Learn more" call to action button

Create a Harbor Crest Vitality Learning Portal account. Get a 14 day free trial to a wealth of learning activities, motivational videos and professional presentations on our learning portal designed specifically to address the eight essential areas of Harbor Crest Vitality.
"Register now" call to action button

Get weekly reports on your progress and goal achievement. Celebrate your success each week as you review your progress on each life balance area.

Appropriate royalty free photos and graphics that fit the chosen theme you recommend.

I'm reviewing the designs. I realize that I need to clarify that Harbor Crest Vitality focuses on eight areas, not just physical fitness and meditation. Spirituality and Sense of Purpose; Fitness and Health; Relationships; Personal Finance; Recreation and Fun; Physical Environment; Personal Development and Learning; Work and Career

1 page

33a6d7
00a990
9bcb3c
2f73b3

```html
<!DOCTYPE html>
<html lang="en">
<head>
<meta charset="utf-8">
<title>Harbor Crest Vitality</title>
<link rel="stylesheet" href="https://fonts.googleapis.com/css2?family=Poppins:wght@300;400;500;600;700&family=Roboto:wght@400;500&display=swap">
<style>
:root{
  --brand:#2f73b3;
  --accent:#33a6d7;
  --ink:#444444;
  --body:#4a4a4a;
  --pale:#eff6f9;
  --pale-2:#eaf1f7;
  --white:#ffffff;
  --video:#000000;
}
*{box-sizing:border-box;margin:0;padding:0}
html,body{width:1200px;height:2484px;overflow:hidden}
body{position:relative;font-family:'Roboto',sans-serif;color:var(--body);background:var(--pale)}
.abs{position:absolute}
.dots{position:absolute;background-image:radial-gradient(circle,var(--accent) 1.4px,transparent 1.8px);background-size:16px 16px}
.btn{position:absolute;display:flex;align-items:center;justify-content:center;font-family:'Poppins',sans-serif;font-size:10.5px;border-radius:2px;color:var(--white);background:var(--accent)}
.photo{position:absolute}

/* hero */
.hero{position:absolute;left:0;top:0;width:1200px;height:561px;background:var(--brand)}
.brand-name{position:absolute;font-family:'Poppins',sans-serif;font-weight:600;color:var(--white)}
.nav a{position:absolute;top:28px;font-family:'Poppins',sans-serif;font-size:10.5px;color:var(--white);text-decoration:none}
.nav .trial{left:900px;top:21px;width:75px;height:24px;background:#6b9bcf;border-radius:2px;display:flex;align-items:center;justify-content:center}
.hero-title{left:224px;top:196px;font-family:'Poppins',sans-serif;font-weight:700;font-size:46px;line-height:53px;color:var(--white);letter-spacing:-1px}
.hero-sub{left:226px;top:316px;font-family:'Poppins',sans-serif;font-size:11.5px;letter-spacing:.6px;color:var(--white)}
.hero .btn{left:226px;top:355px;width:94px;height:31px;background:var(--white);color:var(--brand)}
.video{left:625px;top:190px;width:350px;height:212px;background:var(--video)}

/* sections */
.assess{position:absolute;left:0;top:561px;width:1200px;height:564px;background:var(--pale)}
.trial-sec{position:absolute;left:0;top:1125px;width:1200px;height:561px;background:var(--pale-2)}
.reports{position:absolute;left:0;top:1686px;width:1200px;height:564px;background:var(--pale)}
.assess-title{left:640px;top:202px;font-family:'Poppins',sans-serif;font-weight:300;font-size:25px;line-height:33px;letter-spacing:2.4px;color:var(--ink)}
.copy{font-size:11.5px;line-height:20px;color:var(--body)}
.trial-big{left:224px;top:95px;font-family:'Poppins',sans-serif;font-weight:700;font-size:48px;line-height:58px;color:var(--ink);letter-spacing:1px}
.trial-big span{color:var(--accent)}
.trial-sub{left:224px;top:224px;font-family:'Poppins',sans-serif;font-weight:600;font-size:15.5px;line-height:19px;color:var(--ink);letter-spacing:.3px}
.reports-title{left:664px;top:164px;font-family:'Poppins',sans-serif;font-weight:600;font-size:23px;line-height:27px;letter-spacing:2.4px;color:var(--ink)}
.reports-title span{color:var(--accent)}

/* footer */
.footer{position:absolute;left:0;top:2250px;width:1200px;height:234px;background:var(--brand);color:var(--white)}
.social{position:absolute;top:83px;width:19px;height:19px;border-radius:50%;background:var(--white)}
.col{position:absolute;top:36px;font-size:10px;line-height:24px}
.col h4{font-family:'Poppins',sans-serif;font-weight:600;font-size:12px;margin-bottom:4px}
.copyright{position:absolute;left:0;width:1200px;top:207px;text-align:center;font-size:8.5px}
</style>
</head>
<body>

<header class="hero">
  <div class="brand-name" style="left:225px;top:20px;font-size:16px">Harbor Crest Vitality</div>
  <nav class="nav">
    <a style="left:593px">Assess</a>
    <a style="left:670px">Register</a>
    <a style="left:753px">Contact</a>
    <a style="left:836px">Login</a>
    <a class="trial">Free Trial</a>
  </nav>
  <div class="dots" style="left:590px;top:155px;width:120px;height:120px;mask:linear-gradient(#000,#000) top/100% 22px no-repeat,linear-gradient(#000,#000) left/22px 100% no-repeat;-webkit-mask:linear-gradient(#000,#000) top/100% 22px no-repeat,linear-gradient(#000,#000) left/22px 100% no-repeat"></div>
  <div class="abs" style="left:822px;top:162px;width:162px;height:112px;background:var(--accent)"></div>
  <div class="abs" style="left:608px;top:340px;width:112px;height:80px;border:1.5px solid var(--accent)"></div>
  <div class="abs" style="left:669px;top:380px;width:90px;height:59px;border:1.5px solid var(--accent)"></div>
  <div class="dots" style="left:840px;top:406px;width:130px;height:48px"></div>
  <h1 class="abs hero-title">Harbor Crest<br>Vitality</h1>
  <p class="abs hero-sub">Simple tools to help you live a more balanced life.</p>
  <a class="btn">Learn More</a>
  <div class="abs video">
    <svg width="350" height="212" viewBox="0 0 350 212"><circle cx="175" cy="106" r="26" fill="#fff"/><path d="M168 93 L190 106 L168 119 Z" fill="#000"/></svg>
  </div>
</header>

<section class="assess">
  <div class="dots" style="left:226px;top:116px;width:128px;height:32px"></div>
  <div class="dots" style="left:446px;top:442px;width:128px;height:48px"></div>
  <div class="photo" role="img" aria-label="Mother and daughter stretching together on a red rug in a living room" style="left:224px;top:149px;width:362px;height:289px;border-radius:6px;background:linear-gradient(180deg,#e9e6e1 0%,#d8d3c8 40%,#8a8a72 60%,#b84a3e 85%,#c44b3b 100%)"></div>
  <h2 class="abs assess-title">Assess your current<br>Harbor Crest Vitality</h2>
  <p class="abs copy" style="left:640px;top:279px;width:330px">Complete our free life balance assessment to identify key areas where you you will most benefit.</p>
  <a class="btn" style="left:640px;top:346px;width:93px;height:31px">Learn More</a>
</section>

<section class="trial-sec">
  <h2 class="abs trial-big">Get a 14 day<br><span>free trial</span></h2>
  <h3 class="abs trial-sub">Create a Harbor Crest Vitality<br>Learning Portal account</h3>
  <p class="abs copy" style="left:226px;top:290px;width:380px;line-height:22.5px">Access a wealth of learning activities, motivational videos and professional presentations on our learning portal designed specifically to address the eight essential areas of Harbor Crest Vitality.</p>
  <a class="btn" style="left:226px;top:384px;width:112px;height:31px">Register Now</a>
  <div class="dots" style="left:886px;top:100px;width:124px;height:112px"></div>
  <div class="dots" style="left:664px;top:392px;width:128px;height:32px"></div>
  <div class="abs" style="left:641px;top:143px;width:324px;height:258px;background:#7fc5e3;border-radius:10px"></div>
  <div class="photo" role="img" aria-label="Young man sitting on a city street resting after a run" style="left:651px;top:133px;width:325px;height:258px;border-radius:10px;background:linear-gradient(110deg,#d9d6d0 0%,#eef0f1 35%,#c8cdd2 65%,#e2e4e6 100%)"></div>
</section>

<section class="reports">
  <div class="dots" style="left:480px;top:122px;width:128px;height:112px"></div>
  <div class="dots" style="left:240px;top:316px;width:128px;height:64px"></div>
  <div class="photo" role="img" aria-label="Smiling woman with curly hair looking at her phone against a teal wall" style="left:224px;top:152px;width:375px;height:200px;border-radius:100px;background:linear-gradient(90deg,#3aa3ae 0%,#2c6a63 40%,#4fb4c0 75%,#8fcfd8 100%)"></div>
  <h2 class="abs reports-title">Get weekly reports<br>on your progress and<br><span>achieve your goals</span></h2>
  <p class="abs" style="left:664px;top:271px;width:290px;font-size:12px;line-height:22.5px;color:var(--body)">Celebrate your success each week as you review your progress on each life balance area.</p>
  <a class="btn" style="left:664px;top:332px;width:94px;height:31px">Learn More</a>
</section>

<footer class="footer">
  <div class="brand-name" style="left:226px;top:24px;font-size:16px">Harbor Crest Vitality</div>
  <span class="social" style="left:227px"></span>
  <span class="social" style="left:266px"></span>
  <span class="social" style="left:305px"></span>
  <span class="social" style="left:344px"></span>
  <div class="col" style="left:562px"><h4>Help</h4>Support<br>FAQ<br>Tutorials</div>
  <div class="col" style="left:717px"><h4>Company</h4>About Us<br>Careers<br>Contact Us</div>
  <div class="col" style="left:891px"><h4>Contact</h4>hello@harborcrest.example<br>1.800.555.0187</div>
  <p class="copyright">© Harbor Crest Vitality 2020</p>
</footer>

</body>
</html>
```